Spanish Student Needs a Cover for his PhD Dissertation

Hi everyone :) So, I'm a Corneal surgeon currently finishing my PhD, with a dissertation focused on the evaluation of quality of life in patients affected by a disease called Keratoconus. Just so you know, Keratoconus is a condition in which the cornea (the frontal part of the way) gets thin and bulgy and it decreases vision. What I did during my PhD was designing a questionnaire for evaluating quality of life in this kind of patients.
I need to design a hard cover for my dissertation, which is 200 sheets long. I like kind of minimalistic and geometric designs but I am totally open to suggestions. What needs to be in the cover is the name of the dissertation "Diseño, desarrollo y validación de una encuesta para evaluar el compromiso visual y emocional subjetivos en pacientes con Queratocono" and my name, "Iñigo Tarrasco". The other thing that needs to go there is the logo of my university (Universidad de Montebrisa). Aside from that, anything else is up to the designer. It would be important to use the kind of "red" color I am using in the dissertation. I am attaching the frontal page of my dissertation so you know what kind of design and colors I am using.
In the back part, of the cover, there should be this small inscription: "Iñigo Tarrasco, MD, es un Oftalmólogo Subespecialista en Cirugía Refractiva de la Universidad Serrana Metropolitana (Colombia) y la Universidad de Montebrisa (España). Actualmente se desempeña como miembro del Departamento de Córnea y Cirugía Refractiva de la Clínica de Oftalmología Vallealto y como director de su propia compañía de emprendimiento médico Silver Heron Surgical". Please leave a space to place my picture; I will have it taken this week so I don't have it right now, you can just leave the blank spot and I will include it later
The size of the pages is standard "letter" size.
Thanks a lot!

Target Market(s)

PhD Scholars

Font styles to use
Serif

Requirements
Must have
• The "red" color I use on my font. It must be formal but "young".
Nice to have
• I like to keep the design clean, kind of "formal with a young" touch so to speak. I really like gray colors, so it would be nice to have broad areas of gray. I love geometrical designs.
I have uploaded a very early version a friend of mine made (it even had a different title); this can be a starting point for you to work on, but I am more than open to suggestions and new ideas.
Should not have
• Please don't use my whole name, Iñigo Tarrasco is fine. I don't like ALL CAPITALS.

```html
<!DOCTYPE html>
<html lang="es">
<head>
<meta charset="utf-8">
<title>Cubierta de tesis doctoral – dos propuestas</title>
<link rel="stylesheet" href="https://fonts.googleapis.com/css2?family=Crimson+Text:wght@400;600;700&display=swap">
<style>
  :root {
    --stage: #4f4f4f;
    --cover-grey: #666666;
    --spine-grey: #5a5a5a;
    --deep-red: #a80000;
    --bright-red: #c40006;
    --paper: #ffffff;
    --title-light: #ececec;
    --label: #a9a9a9;
    --photo-light: #e6e6e6;
    --photo-mid: #9a9a9a;
    --photo-dark: #3c3c3c;
  }
  html, body {
    margin: 0;
    padding: 0;
    width: 1200px;
    height: 794px;
    overflow: hidden;
    background: var(--stage);
  }
  .presentation {
    display: block;
    width: 1200px;
    height: 794px;
    font-family: "Crimson Text", Georgia, serif;
  }
  .option-label { fill: var(--label); font-size: 34px; letter-spacing: 1px; }
  .title-light { fill: var(--title-light); font-size: 27px; font-weight: 400; }
  .title-bold  { fill: var(--paper); font-size: 28px; font-weight: 700; }
  .title-bold-lg { fill: var(--paper); font-size: 31px; font-weight: 700; }
  .author-red { fill: var(--deep-red); font-size: 33px; letter-spacing: 7px; }
  .author-white { fill: var(--paper); font-size: 23px; letter-spacing: 10px; }
  .brand-name { fill: var(--deep-red); font-size: 44px; font-weight: 700; }
  .brand-name-sm { fill: var(--deep-red); font-size: 34px; font-weight: 700; }
  .brand-sub { fill: #222; font-size: 14px; }
  .brand-sub-sm { fill: #222; font-size: 11px; }
  .uni-name { fill: var(--paper); font-size: 15px; font-weight: 700; }
  .uni-name-lg { fill: var(--paper); font-size: 17px; font-weight: 700; }
</style>
</head>
<body>
<svg class="presentation" viewBox="0 0 2000 1323" preserveAspectRatio="none" xmlns="http://www.w3.org/2000/svg">
  <defs>
    <linearGradient id="eye-photo" x1="0" y1="0" x2="1" y2="1">
      <stop offset="0" stop-color="var(--photo-mid)"/>
      <stop offset="0.45" stop-color="var(--photo-dark)"/>
      <stop offset="1" stop-color="var(--photo-light)"/>
    </linearGradient>
    <linearGradient id="eye-photo-soft" x1="0" y1="0" x2="1" y2="1">
      <stop offset="0" stop-color="var(--photo-light)"/>
      <stop offset="0.5" stop-color="var(--photo-mid)"/>
      <stop offset="1" stop-color="var(--paper)"/>
    </linearGradient>
    <filter id="cover-shadow" x="-10%" y="-10%" width="120%" height="120%">
      <feDropShadow dx="0" dy="8" stdDeviation="14" flood-color="#000" flood-opacity="0.45"/>
    </filter>
  </defs>

  <rect width="2000" height="1323" fill="var(--stage)"/>

  <!-- Option 1 -->
  <text class="option-label" x="180" y="90">OPTION-1</text>
  <g class="cover cover-one">
    <rect x="168" y="142" width="806" height="1042" fill="var(--cover-grey)" filter="url(#cover-shadow)"/>
    <polygon points="695,142 974,142 974,408 815,262" fill="var(--deep-red)"/>
    <g role="img" aria-label="Fotografía en blanco y negro de un ojo en primer plano">
      <polygon points="815,262 974,410 974,1184 555,1184 228,855" fill="url(#eye-photo)"/>
    </g>
    <polygon points="168,912 228,855 555,1184 168,1184" fill="var(--deep-red)"/>
    <rect class="spine" x="168" y="142" width="60" height="1042" fill="var(--spine-grey)" opacity="0.55"/>
    <line x1="226" y1="142" x2="226" y2="1184" stroke="#777" stroke-width="2"/>

    <g class="school-mark">
      <rect x="241" y="160" width="363" height="82" fill="var(--paper)"/>
      <text class="brand-name" x="422" y="207" text-anchor="middle">EDMonte</text>
      <text class="brand-sub" x="422" y="229" text-anchor="middle">Escuela de Doctorado Universidad de Montebrisa</text>
    </g>
    <g class="university-mark">
      <circle cx="886" cy="187" r="31" fill="var(--paper)" stroke="var(--bright-red)" stroke-width="3"/>
      <text class="uni-name" x="886" y="233" text-anchor="middle">Universidad de Montebrisa</text>
    </g>

    <g class="thesis-title">
      <text class="title-light" x="227" y="330">DISEÑO, DESARROLLO Y</text>
      <text class="title-light" x="227" y="372">VALIDACIÓN DE UNA ENCUESTA</text>
      <text class="title-light" x="227" y="414">PARA EVALUAR EL COMPROMISO</text>
      <text class="title-bold" x="227" y="458">VISUAL Y EMOCIONAL</text>
      <text class="title-bold" x="227" y="502">SUBJETIVOS EN PACIENTES</text>
      <text class="title-bold" x="227" y="546">CON QUERATOCONO</text>
    </g>
    <text class="author-red" x="725" y="1100" text-anchor="middle">Iñigo Tarrasco</text>
  </g>

  <!-- Option 2 -->
  <text class="option-label" x="1058" y="90">OPTION-2</text>
  <g class="cover cover-two">
    <rect x="1058" y="146" width="751" height="1028" fill="var(--cover-grey)" filter="url(#cover-shadow)"/>
    <polygon points="1058,425 1445,146 1809,146 1809,478 1290,955 1058,1165" fill="var(--bright-red)"/>
    <rect class="spine" x="1058" y="146" width="65" height="1028" fill="var(--spine-grey)" opacity="0.45"/>

    <g class="diamonds">
      <polygon points="1322,517 1422,617 1322,717 1222,617" fill="var(--cover-grey)"/>
      <polygon points="1433,480 1498,545 1433,610 1368,545" fill="#dddddd"/>
      <polygon points="1590,480 1750,617 1590,775 1440,617" fill="var(--deep-red)"/>
      <g role="img" aria-label="Detalle desenfocado de un ojo">
        <polygon points="1590,472 1735,617 1590,762 1445,617" fill="url(#eye-photo-soft)"/>
      </g>
      <polygon points="1435,620 1680,855 1435,1095 1195,855" fill="var(--deep-red)"/>
      <g role="img" aria-label="Fotografía en blanco y negro de un ojo en primer plano">
        <polygon points="1435,630 1665,855 1435,1080 1205,855" fill="url(#eye-photo)"/>
      </g>
      <polygon points="1435,655 1635,855 1435,1055 1235,855" fill="none" stroke="var(--paper)" stroke-width="4"/>
      <polygon points="1185,1010 1250,1070 1185,1135 1120,1070" fill="var(--deep-red)"/>
      <g role="img" aria-label="Detalle pequeño de un ojo">
        <polygon points="1185,1010 1240,1065 1185,1120 1130,1065" fill="url(#eye-photo-soft)"/>
      </g>
      <g role="img" aria-label="Detalle pequeño de un ojo">
        <polygon points="1709,948 1754,993 1709,1038 1664,993" fill="url(#eye-photo-soft)"/>
      </g>
      <g role="img" aria-label="Detalle recortado de un ojo">
        <polygon points="1809,1025 1809,1174 1740,1174 1700,1135" fill="url(#eye-photo-soft)"/>
      </g>
    </g>

    <g class="school-mark">
      <rect x="1515" y="158" width="273" height="62" fill="var(--paper)"/>
      <text class="brand-name-sm" x="1651" y="195" text-anchor="middle">EDMonte</text>
      <text class="brand-sub-sm" x="1651" y="212" text-anchor="middle">Escuela de Doctorado Universidad de Montebrisa</text>
    </g>
    <g class="university-mark">
      <circle cx="1181" cy="201" r="36" fill="var(--paper)" stroke="var(--bright-red)" stroke-width="3"/>
      <text class="uni-name-lg" x="1181" y="259" text-anchor="middle">Universidad de Montebrisa</text>
    </g>

    <g class="thesis-title" text-anchor="middle">
      <text class="title-light" x="1520" y="288">DISEÑO, DESARROLLO Y VALIDACIÓN</text>
      <text class="title-light" x="1520" y="323">DE UNA ENCUESTA PARA EVALUAR EL</text>
      <text class="title-bold-lg" x="1520" y="363">COMPROMISO VISUAL Y EMOCIONAL</text>
      <text class="title-bold-lg" x="1520" y="405">SUBJETIVOS EN PACIENTES CON</text>
      <text class="title-bold-lg" x="1520" y="447">QUERATOCONO</text>
    </g>
    <text class="author-white" x="1435" y="1124" text-anchor="middle">Iñigo Tarrasco</text>
  </g>
</svg>
</body>
</html>
```